New Business Card Design*

We are a recruitment company based in Norwich/Cambridge England.
I have included our company logo which we want to remain the same.

What we are looking for is a new creative Business card which will really stand out!!

Contact Information for Business Card

Harriet Dunmore
email: Harriet@vexalim.co.uk
Address: Larkwell House
Brambleton Enterprise Quarter
Thistlebrook Road
Norwich
QX9 2LB
Tel:01632 418305

```html
<!DOCTYPE html>
<html lang="en">
<head>
<meta charset="utf-8">
<title>Vexalim Business Card</title>
<link href="https://fonts.googleapis.com/css2?family=Open+Sans:wght@400;600;700&family=Montserrat:wght@400;600&display=swap" rel="stylesheet">
<style>
  :root {
    --stage: #2b2b2d;
    --card-grey: #8e8a92;
    --card-white: #ffffff;
    --brand-green: #8cc540;
    --brand-grey: #8e8a92;
    --ink: #1e1e1e;
    --rule: #6f6f6f;
    --on-grey: #ffffff;
  }
  * { margin: 0; padding: 0; box-sizing: border-box; }
  html, body { width: 1200px; height: 900px; overflow: hidden; }
  body {
    background: var(--stage);
    font-family: "Open Sans", Arial, sans-serif;
    position: relative;
  }
  .card {
    position: absolute;
    left: 250px;
    width: 700px;
    height: 400px;
    box-shadow: 0 10px 30px rgba(0,0,0,.45);
  }
  .card--back { top: 36px; background: var(--card-grey); }
  .card--front { top: 464px; background: var(--card-white); }

  .back-mark {
    position: absolute;
    top: 148px; left: 0; right: 0;
    display: flex; align-items: center; justify-content: center; gap: 18px;
  }
  .back-mark__dot { width: 56px; height: 56px; border-radius: 50%; background: var(--brand-green); }
  .back-mark__name {
    font-family: "Montserrat", Arial, sans-serif;
    font-weight: 600; font-size: 56px; color: var(--on-grey); letter-spacing: 0.5px;
  }
  .back-web {
    position: absolute; bottom: 38px; left: 0; right: 0; text-align: center;
    font-family: "Montserrat", Arial, sans-serif;
    font-size: 15px; letter-spacing: 4px; color: var(--on-grey);
  }
  .back-web b { font-weight: 600; }

  .front-mark {
    position: absolute; left: 60px; top: 90px; width: 230px;
    display: flex; flex-direction: column; align-items: center; gap: 18px;
  }
  .front-mark__dot { width: 160px; height: 160px; border-radius: 50%; background: var(--brand-green); }
  .front-mark__name { font-weight: 700; font-size: 30px; color: var(--brand-grey); }

  .details {
    position: absolute; left: 340px; top: 70px; bottom: 70px;
    border-left: 2px solid var(--rule);
    padding-left: 20px;
    color: var(--ink);
  }
  .details__name { font-weight: 700; font-size: 34px; letter-spacing: 1px; line-height: 1; text-transform: uppercase; }
  .details__role { font-weight: 600; font-size: 17px; text-transform: uppercase; margin-top: 4px; }
  .details__address { font-size: 14px; line-height: 1.35; margin-top: 14px; }
  .contact { list-style: none; margin-top: 12px; font-size: 16px; }
  .contact li { display: flex; align-items: center; gap: 10px; line-height: 1.6; }
  .contact svg { width: 16px; height: 16px; flex: none; }
  .accent { color: var(--brand-green); }
</style>
</head>
<body>
  <section class="card card--back" aria-label="Card back">
    <div class="back-mark">
      <span class="back-mark__dot"></span>
      <span class="back-mark__name">Vexalim</span>
    </div>
    <p class="back-web">www.<b>vexalimrecruit</b>.com</p>
  </section>

  <section class="card card--front" aria-label="Card front">
    <div class="front-mark">
      <span class="front-mark__dot"></span>
      <span class="front-mark__name">Vexalim</span>
    </div>
    <div class="details">
      <h1 class="details__name">Harriet Dunmore</h1>
      <p class="details__role">CEO &amp; Founder</p>
      <p class="details__address">Larkwell House Brambleton Enterprise Quarter,<br>Thistlebrook Road Norwich, QX9 2LB</p>
      <ul class="contact">
        <li>
          <svg viewBox="0 0 16 16" aria-hidden="true"><path d="M4 1 L6.5 4.5 L5 6 Q6.5 9.5 10 11 L11.5 9.5 L15 12 L13 15 Q5 14 1 3 Z" fill="var(--brand-green)"/></svg>
          01632 418305
        </li>
        <li>
          <svg viewBox="0 0 16 16" aria-hidden="true"><rect x="1" y="3" width="14" height="10" fill="var(--brand-green)"/><path d="M1 3 L8 9 L15 3" fill="none" stroke="#fff" stroke-width="1.4"/></svg>
          Harriet@vexalim.co.uk
        </li>
        <li>
          <svg viewBox="0 0 16 16" aria-hidden="true"><circle cx="9.5" cy="6.5" r="4.5" fill="none" stroke="var(--brand-green)" stroke-width="2"/><line x1="6" y1="10" x2="1.5" y2="14.5" stroke="var(--brand-green)" stroke-width="2.2"/></svg>
          <span>www.<span class="accent">vexalimrecruit</span>.com</span>
        </li>
      </ul>
    </div>
  </section>
</body>
</html>
```